Business Card Design job - Tyre Shop

Client wants a double sided business cards designed for a Tyre Shop.

The logo can be used in multiple ways, some examples are attached.

The reference font is:
https://www.typebarrow.com/fonts/open-sans
Others can be applied.

Color scheme should be mainly black and white, and red as a third less used color.

Contact Information for Business Card

Required Fields (Portuguese language):
- Name "Augusto Melro"
- Title "Gerente"
- Phone "253 704 862"
- Website "www.rodaslume.pt"
- Email "geral@rodaslume.pt
- Address "Rua da Fonteira N.187
4730-512 Fonteluz, Valmira"

Font styles to use
Sans Serif

Requirements
Must have
• Corporate Logo
Nice to have
• The client would like the card to have special feature to measure the tyre tread, as shown in examples attached.
• The tread Values as Portuguese law are:
• - Ilegal - less than 1.6mm
• - change tyres - between 3mm and 1.6 mm
• - OK - above 3mm
• Card should be kept standard rectangle size 85x55mm

```html
<!DOCTYPE html>
<html lang="pt">
<head>
<meta charset="utf-8">
<title>Rodas Lume — Cartão de Visita</title>
<link href="https://fonts.googleapis.com/css2?family=Open+Sans:wght@400;600;700;800&display=swap" rel="stylesheet">
<style>
  :root {
    --ink: #0b0b0b;
    --paper: #ffffff;
    --backdrop: #a9a9a9;
  }
  * { box-sizing: border-box; margin: 0; padding: 0; }
  html, body { width: 1200px; height: 1200px; overflow: hidden; }
  body {
    background: var(--backdrop);
    font-family: "Open Sans", Arial, sans-serif;
    position: relative;
  }
  .card {
    position: absolute;
    left: 190px;
    width: 820px;
    height: 531px;
    overflow: hidden;
  }
  .card--front { top: 45px; background: var(--ink); color: var(--paper); }
  .card--back { top: 624px; background: var(--paper); color: var(--ink); }

  .brand { position: absolute; display: flex; align-items: center; gap: 18px; }
  .brand__dot { border-radius: 50%; flex: none; }
  .brand__name { font-weight: 800; line-height: 1; letter-spacing: 0.5px; }

  .card--front .brand { left: 170px; top: 82px; }
  .card--front .brand__dot { width: 74px; height: 74px; background: var(--paper); }
  .card--front .brand__name { font-size: 58px; color: var(--paper); }
  .tagline {
    position: absolute; left: 262px; top: 150px;
    font-size: 10px; font-weight: 700; letter-spacing: 3.2px;
    color: var(--paper); text-transform: uppercase;
  }

  .name-band {
    position: absolute; left: 0; top: 292px; width: 596px; height: 50px;
    background: var(--paper); color: var(--ink);
    display: flex; align-items: center; justify-content: flex-end;
    padding-right: 24px; gap: 14px;
  }
  .name-band__name { font-size: 30px; font-weight: 700; }
  .name-band__rule { width: 3px; height: 30px; background: var(--ink); }
  .name-band__title { font-size: 21px; font-weight: 400; }
  .chevrons { position: absolute; }
  .card--front .chevrons { left: 602px; top: 294px; }

  .contact { position: absolute; top: 428px; font-size: 20px; line-height: 29px; white-space: nowrap; }
  .contact--address { left: 113px; }
  .contact--lines { left: 422px; }
  .contact strong { font-weight: 700; }
  .contact-rule {
    position: absolute; left: 398px; top: 432px;
    width: 2px; height: 54px; background: var(--paper);
  }

  .card--back .brand { left: 275px; top: 95px; }
  .card--back .brand__name { font-size: 50px; color: var(--ink); }
  .card--back .brand__dot { width: 150px; height: 150px; background: var(--ink); }
  .web-band {
    position: absolute; left: 0; top: 470px; width: 673px; height: 36px;
    background: var(--ink); color: var(--paper);
    display: flex; align-items: center; justify-content: flex-end;
    padding-right: 30px;
    font-size: 18px; font-weight: 600; letter-spacing: 11px;
  }
  .card--back .chevrons { left: 678px; top: 465px; }
</style>
</head>
<body>

<section class="card card--front" aria-label="Frente do cartão">
  <div class="brand">
    <span class="brand__dot"></span>
    <span class="brand__name">RODAS LUME</span>
  </div>
  <p class="tagline">Especialista em pneus &amp; manutenção automóvel</p>

  <div class="name-band">
    <span class="name-band__name">Augusto Melro</span>
    <span class="name-band__rule"></span>
    <span class="name-band__title">Gerente</span>
  </div>
  <svg class="chevrons" width="150" height="46" viewBox="0 0 150 46" aria-hidden="true">
    <g fill="none" stroke="#ffffff" stroke-width="7" stroke-linejoin="miter">
      <polyline points="10,8 25,23 10,38"/>
      <polyline points="40,8 55,23 40,38"/>
      <polyline points="70,8 85,23 70,38"/>
      <polyline points="100,8 115,23 100,38"/>
    </g>
  </svg>

  <p class="contact contact--address">Rua da Fonteira N.187<br>4730-512 Fonteluz, Valmira</p>
  <span class="contact-rule"></span>
  <p class="contact contact--lines"><strong>Phone:</strong> 253 704 862<br><strong>Email:</strong> geral@rodaslume.pt</p>
</section>

<section class="card card--back" aria-label="Verso do cartão">
  <div class="brand">
    <span class="brand__name">RODAS<br>LUME</span>
    <span class="brand__dot"></span>
  </div>

  <div class="web-band">www.rodaslume.pt</div>
  <svg class="chevrons" width="110" height="46" viewBox="0 0 110 46" aria-hidden="true">
    <g fill="none" stroke="#0b0b0b" stroke-width="6" stroke-linejoin="miter">
      <polyline points="8,12 19,23 8,34"/>
      <polyline points="32,12 43,23 32,34"/>
      <polyline points="56,12 67,23 56,34"/>
      <polyline points="80,12 91,23 80,34"/>
    </g>
  </svg>
</section>

</body>
</html>
```